Vitamin and Nutrition Ecommerce Site Needs a High End Website Design

We need a new and improved Homepage design for a leading Vitamin eCommerce business.
We supply our customers worldwide with leading brands of vitamin supplements and nutritional products at discounted prices.
The site design and layout must improve sales conversion and maximize the user experience staying on the site!

We will need to see;
A New Nutri Harbour stylized font (no logo)
High-End Modern Design
Easy Sales Conversion Experience
Excellent Layout, Fast Navigation
Quality Font style, Stylish Colour Palette Selection
Appropriate Spacing
Call To Action to Improve Sales Conversion
Web page should Look Clean and Minimalist

The design should improve sales, communicate easy to find products, facilitate fast ordering, have a modern and professional appearance centered toward a predominately female consumer.

Thank you for your interest in this project!

Current design can be found on this link;
www.nutriharbour.com.au/nutri/

Target Market(s)

80% Female 30-65 years

Industry/Entity Type

Business

Number of Pages Required

1 page

Colors

Designer to choose colors to be used in the design.

Requirements
Must have
• design must result improve sales conversion
• new Nutri Harbour font design
• search field
• attractive clean modern design
• stylish font and colour palette selection
Nice to have
• white background
Should not have
• cluttered or busy layout
• confusing navigation

```html
<!DOCTYPE html>
<html lang="en">
<head>
<meta charset="utf-8">
<title>Nutri Harbour – Home</title>
<link rel="stylesheet" href="https://fonts.googleapis.com/css2?family=Lobster+Two:wght@400;700&family=Roboto:wght@300;400;500;700&display=swap">
<style>
:root{
  --green:#7fa83a;
  --green-dark:#4d7a1f;
  --green-deep:#3f6a18;
  --text:#222;
  --muted:#9a9a9a;
  --line:#d9d9d9;
  --soft:#f4f4f4;
  --card-green:#74c07e;
  --card-gold:#cdbb5a;
  --card-blue:#73c0e2;
  --footer-bottom:#2b2b2b;
}
*{margin:0;padding:0;box-sizing:border-box}
html,body{width:1200px;height:2804px;overflow:hidden;background:#fff}
body{position:relative;font-family:"Roboto",sans-serif;color:var(--text)}
.abs{position:absolute}
.script{font-family:"Lobster Two",cursive;font-weight:700}

/* top bar */
.topbar{left:0;top:0;width:1200px;height:30px;border-bottom:1px solid #e6e6e6;font-size:15px;color:var(--muted)}
.topbar .call{left:30px;top:6px}
.topbar .account{right:30px;top:6px;display:flex;align-items:center;gap:6px}

/* header */
.brand{left:30px;top:62px;display:flex;align-items:center;gap:10px;font-size:38px;font-weight:500;color:var(--green)}
.brand .dot{width:22px;height:22px;border-radius:50%;background:var(--green)}
.search{left:374px;top:66px;width:616px;height:44px;background:var(--soft);border-radius:3px;font-size:16px;color:#888;padding:12px 18px}
.search svg{position:absolute;right:16px;top:13px}
.icon-heart{left:1044px;top:72px}
.icon-cart{left:1112px;top:68px}
.cart-count{left:1144px;top:52px;width:22px;height:22px;border-radius:50%;background:#111;color:#fff;font-size:13px;text-align:center;line-height:22px}

/* nav */
.nav{left:0;top:138px;width:1200px;height:70px;background:var(--green)}
.nav .all-cats{left:30px;top:0;width:262px;height:70px;background:var(--green-deep);color:#fff;font-size:22px;text-align:center;line-height:70px}
.nav ul{position:absolute;left:318px;top:0;display:flex;list-style:none;gap:31px;height:70px;align-items:center;color:#fff;font-size:16px;font-weight:500}

/* categories + hero */
.cats{left:30px;top:208px;width:262px;height:426px;border:1px solid var(--line);border-top:none}
.cats li{list-style:none;height:39.5px;border-bottom:1px solid var(--line);font-size:14px;color:#444;padding:11px 12px;position:relative}
.cats li.sub::after{content:"";position:absolute;right:14px;top:15px;width:7px;height:7px;border-right:1.5px solid #888;border-top:1.5px solid #888;transform:rotate(45deg)}
.hero{left:292px;top:208px;width:878px;height:426px;background:radial-gradient(ellipse 60% 55% at center,#e6cba0 0%,#dcbb88 45%,#b98c55 70%,#6f8a34 90%,#4a6420 100%)}
.hero-copy{left:292px;top:338px;width:878px;text-align:center}
.hero-copy h1{font-size:56px;line-height:66px;color:var(--green-dark);font-family:"Lobster Two",cursive;font-weight:700}
.hero-copy p{font-size:20px;font-weight:700;color:#111;margin-top:2px}
.btn-shop{display:inline-block;margin-top:16px;background:#8cc152;color:#fff;font-size:17px;font-weight:500;padding:10px 42px}

/* new products */
.newprod{left:0;top:656px;width:1200px;height:522px;background:#f6f6f6}
.section-title{width:1200px;text-align:center;font-size:36px;color:#111}
.pcard{top:108px;width:256px;height:366px;text-align:center;color:#fff}
.pcard h3{font-family:"Lobster Two",cursive;font-weight:700;font-size:30px;margin-top:66px}
.pcard p{font-size:22px;font-weight:300;margin-top:6px}
.pcard .fruit{position:absolute;left:-8px;bottom:-10px;width:272px;height:170px;border-radius:60px 60px 30px 30px;background:radial-gradient(ellipse at 50% 60%,#f2a12a 0%,#d9662a 45%,#7c8e2a 80%,rgba(124,142,42,0) 100%)}
.chev{top:240px}

/* why choose */
.why-title{left:120px;top:1222px;font-size:36px;color:#111}
.why-item{left:130px;width:400px}
.why-item h4{font-size:17px;font-weight:500;margin-left:70px}
.why-item p{font-size:13px;color:#777;line-height:19px;margin-left:74px;margin-top:8px}
.why-item svg{position:absolute;left:0;top:0}
.yoga{left:650px;top:1228px;width:430px;height:400px;background:radial-gradient(ellipse 45% 50% at 50% 48%,#f0cfc4 0%,#e8b9c9 40%,#7a6a70 75%,rgba(255,255,255,0) 100%)}

/* tabs */
.tabs{left:0;top:1696px;width:1200px;text-align:center;font-size:30px}
.tabs span{margin:0 14px;color:#111}
.tabs span.active{color:var(--green)}

/* product strip */
.strip{left:116px;top:1776px;width:968px;height:262px;border:1px solid var(--line)}
.sale{left:0;top:0;width:202px;height:260px;background:linear-gradient(160deg,var(--green-deep),#8cbd3f)}
.sale .pct{position:absolute;left:24px;top:30px;color:#fff;font-family:"Lobster Two",cursive;font-weight:700;font-size:56px}
.sale .pct small{font-size:30px}
.sale .rule{position:absolute;left:24px;top:108px;width:150px;height:3px;background:#fff}
.sale .fruit{position:absolute;left:30px;top:130px;width:150px;height:112px;border-radius:50%;background:radial-gradient(ellipse,#f2c02a 0%,#e08a2a 50%,rgba(224,138,42,0) 72%)}
.item{top:0;width:192px;height:260px;border-left:1px solid var(--line);text-align:center}
.item .shot{margin:36px auto 0;width:110px;height:120px;border-radius:8px}
.item .name{font-size:13px;margin-top:18px;color:#222}
.item .stars{color:#f2c21a;font-size:22px;letter-spacing:1px;margin-top:4px}
.item .price{font-size:18px;color:var(--green);margin-top:2px}
.next-box{left:924px;top:94px;width:44px;height:52px;background:#8cc152}
.next-box svg{margin:16px 0 0 14px}

/* panels */
.panel{top:2100px;height:300px;border:1px solid var(--line)}
.panel h3{position:absolute;left:22px;top:18px;font-size:26px;color:#111}
.panel .arrows{position:absolute;top:22px;display:flex;gap:8px}
.arrow-dot{width:24px;height:24px;border-radius:50%;background:var(--green);display:flex;align-items:center;justify-content:center}
.skin-text{position:absolute;left:24px;top:64px;width:222px;font-size:13px;line-height:19px;color:#aaa}
.btn-more{position:absolute;left:24px;top:212px;background:var(--green-dark);color:#fff;font-size:14px;font-weight:500;padding:10px 26px}
.skin-photo{position:absolute;left:262px;top:62px;width:190px;height:226px;background:radial-gradient(ellipse 50% 50% at 55% 45%,#f2dcd0 0%,#e9c7b6 45%,#bcd89a 80%,rgba(255,255,255,0) 100%)}
.quote{position:absolute;left:28px;top:72px;width:404px;height:106px;background:#8cb14b;color:#fff;font-style:italic;font-size:13px;line-height:19px;padding:10px 14px}
.quote::after{content:"";position:absolute;right:48px;bottom:-12px;border-left:12px solid transparent;border-right:12px solid transparent;border-top:12px solid #8cb14b}
.who{position:absolute;right:116px;top:222px;text-align:right;font-size:13px}
.who span{display:block;color:var(--green);margin-top:3px}
.avatar{position:absolute;right:38px;top:200px;width:70px;height:70px;border-radius:50%;background:linear-gradient(#d9d9d9,#b9b9b9)}

/* brands */
.brands{left:116px;top:2460px;width:968px;height:60px}
.brand-name{top:0;height:60px;width:160px;display:flex;align-items:center;justify-content:center;font-size:24px;font-weight:400;color:#333}

/* footer */
.footer{left:0;top:2566px;width:1200px;height:204px;background:var(--green);color:#fff}
.fcol{top:30px}
.fcol h5{font-size:16px;font-weight:700;margin-bottom:12px}
.fcol li{list-style:none;font-size:13px;line-height:19px}
.news{left:498px;top:2614px;width:328px;height:40px;background:#fff;font-size:13px;font-style:italic;color:#aaa;padding:11px 14px}
.news .send{position:absolute;right:0;top:0;width:56px;height:40px;background:#fff;border-left:1px solid #ddd}
.social{left:874px;top:2626px;display:flex;gap:12px}
.social span{width:36px;height:36px;border-radius:50%;background:#2b2b2b;display:block}
.bottombar{left:0;top:2770px;width:1200px;height:34px;background:var(--footer-bottom);color:#fff;font-size:13px}
.bottombar .copy{left:118px;top:9px}
.pay{right:100px;top:9px;display:flex;gap:6px}
.pay span{width:28px;height:16px;background:#fff;border-radius:2px;display:block}
</style>
</head>
<body>

<div class="abs topbar">
  <div class="abs call">Call Us: +0123 456 789</div>
  <div class="abs account">
    <svg width="12" height="14" viewBox="0 0 12 14"><circle cx="6" cy="4" r="3.5" fill="#7fa83a"/><path d="M0 14c0-4 3-6 6-6s6 2 6 6z" fill="#7fa83a"/></svg>
    My Account ▾
  </div>
</div>

<div class="abs brand"><span class="dot"></span>Nutri Harbour</div>

<div class="abs search">Search here
  <svg width="18" height="18" viewBox="0 0 18 18"><circle cx="7.5" cy="7.5" r="5.5" fill="none" stroke="#7fa83a" stroke-width="2.4"/><path d="M11.5 11.5l5 5" stroke="#7fa83a" stroke-width="2.4"/></svg>
</div>
<svg class="abs icon-heart" width="36" height="32" viewBox="0 0 36 32"><path d="M18 31L4 17C-1 12 1 3 9 2c4 0 7 3 9 5 2-2 5-5 9-5 8 1 10 10 5 15z" fill="#7fa83a"/></svg>
<svg class="abs icon-cart" width="44" height="40" viewBox="0 0 44 40"><path d="M2 4h7l5 22h24l4-16H12" fill="none" stroke="#7fa83a" stroke-width="3.5" stroke-linejoin="round"/><path d="M14 14h26M15 20h24" stroke="#7fa83a" stroke-width="2"/><circle cx="17" cy="34" r="3.5" fill="#7fa83a"/><circle cx="35" cy="34" r="3.5" fill="#7fa83a"/></svg>
<div class="abs cart-count">0</div>

<nav class="abs nav">
  <div class="abs all-cats">All Categories</div>
  <ul><li>HOME</li><li>ABOUT US</li><li>PRODUCTS</li><li>FEATURED PRODUCTS</li><li>BLOG</li><li>SERVICES</li><li>CONTACT US</li></ul>
</nav>

<ul class="abs cats">
  <li class="sub">Brand</li><li class="sub">Supplements</li><li class="sub">Sports Nutrition</li><li>Hair Care</li><li>Chiropractic Pillows</li><li>Health Condition</li><li>Beauty &amp; Skin care</li><li>Gluten Free</li><li>Skin care</li>
</ul>

<div class="abs hero" role="img" aria-label="Overhead photo of fresh fruit and vegetables around a wooden board"></div>
<div class="abs hero-copy">
  <h1>Nutri Harbour</h1>
  <p>Loren ipsum Dolar Sit Amet Consiclet</p>
  <span class="btn-shop">SHOP NOW</span>
</div>

<section class="abs newprod">
  <h2 class="abs section-title script" style="top:28px">New Products</h2>
  <svg class="abs chev" style="left:84px" width="30" height="56" viewBox="0 0 30 56"><path d="M27 2L3 28l24 26" fill="none" stroke="#111" stroke-width="3"/></svg>
  <svg class="abs chev" style="left:1082px" width="30" height="56" viewBox="0 0 30 56"><path d="M3 2l24 26L3 54" fill="none" stroke="#111" stroke-width="3"/></svg>
  <div class="abs pcard" style="left:158px;background:var(--card-green)"><h3>Sports Condition</h3><p>17 Products</p><div class="fruit" role="img" aria-label="Juice bottle surrounded by tropical fruit"></div></div>
  <div class="abs pcard" style="left:474px;background:var(--card-gold)"><h3>Health Condition</h3><p>20 Products</p><div class="fruit" role="img" aria-label="Juice bottle surrounded by tropical fruit"></div></div>
  <div class="abs pcard" style="left:785px;background:var(--card-blue)"><h3>Beauty &amp; Skin Care</h3><p>30 Products</p><div class="fruit" role="img" aria-label="Juice bottle surrounded by tropical fruit"></div></div>
</section>

<h2 class="abs why-title script">Why Choose Us</h2>
<div class="abs why-item" style="top:1296px">
  <svg width="46" height="40" viewBox="0 0 46 40"><rect x="0" y="16" width="10" height="22" fill="#7fa83a"/><path d="M14 18l10-16c4 0 5 4 4 8l-2 6h14c4 0 5 4 3 6l-4 14H14z" fill="#7fa83a"/></svg>
  <h4>Verified Trusted Store</h4>
  <p>It is a long established fact that a reader will be distracted by the readable content of a page when looking at its layout.</p>
</div>
<div class="abs why-item" style="top:1412px">
  <svg width="56" height="40" viewBox="0 0 56 40"><rect x="0" y="6" width="32" height="24" rx="2" fill="#7fa83a"/><path d="M34 12h12l8 10v8H34z" fill="#7fa83a"/><circle cx="12" cy="33" r="5" fill="#7fa83a" stroke="#fff" stroke-width="2"/><circle cx="44" cy="33" r="5" fill="#7fa83a" stroke="#fff" stroke-width="2"/></svg>
  <h4>Free Shipping</h4>
  <p>It is a long established fact that a reader will be distracted by the readable content of a page when looking at its layout.</p>
</div>
<div class="abs why-item" style="top:1538px">
  <svg width="50" height="56" viewBox="0 0 50 56"><circle cx="25" cy="18" r="11" fill="#7fa83a"/><path d="M11 18a14 14 0 0128 0" fill="none" stroke="#7fa83a" stroke-width="3"/><path d="M4 56c0-14 9-22 21-22s21 8 21 22z" fill="#7fa83a"/></svg>
  <h4>Customer Support</h4>
  <p>It is a long established fact that a reader will be distracted by the readable content of a page when looking at its layout.</p>
</div>
<div class="abs yoga" role="img" aria-label="Woman in pink top meditating in a cross-legged yoga pose"></div>

<div class="abs tabs script"><span class="active">Our Product</span><span>Sale</span><span>Recommended</span></div>

<div class="abs strip">
  <div class="abs sale"><div class="pct">50%<small> off</small></div><div class="rule"></div><div class="fruit" role="img" aria-label="Pile of tropical fruit"></div></div>
  <div class="abs item" style="left:202px"><div class="shot" role="img" aria-label="Three amber supplement jars" style="background:linear-gradient(#6b4a22,#9b6a30)"></div><div class="name">LOREN IPSUM DOLAR</div><div class="stars">★★★★★</div><div class="price">$60.00</div></div>
  <div class="abs item" style="left:394px"><div class="shot" role="img" aria-label="Dark supplement bottle" style="width:60px;background:linear-gradient(#2a1d15,#6a2b1a)"></div><div class="name">LOREN IPSUM DOLAR</div><div class="stars">★★★★★</div><div class="price">$70.00</div></div>
  <div class="abs item" style="left:586px"><div class="shot" role="img" aria-label="White supplement bottle with tablets" style="width:70px;background:linear-gradient(#f2f2f2,#cfd8c8)"></div><div class="name">LOREN IPSUM DOLAR</div><div class="stars">★★★★★</div><div class="price">$80.00</div></div>
  <div class="abs item" style="left:778px"><div class="shot" role="img" aria-label="Orange skin care tube" style="width:56px;background:linear-gradient(#f6b04a,#ea6a20)"></div><div class="name">LOREN IPSUM DOLAR</div><div class="stars">★★★★★</div><div class="price">$90.00</div></div>
  <div class="abs next-box"><svg width="14" height="20" viewBox="0 0 14 20"><path d="M2 2l9 8-9 8" fill="none" stroke="#fff" stroke-width="3"/></svg></div>
</div>

<div class="abs panel" style="left:116px;width:462px">
  <h3 class="script">Skin Care</h3>
  <div class="arrows" style="right:20px"><span class="arrow-dot"><svg width="8" height="12" viewBox="0 0 8 12"><path d="M6 1L2 6l4 5" fill="none" stroke="#fff" stroke-width="2.2"/></svg></span><span class="arrow-dot"><svg width="8" height="12" viewBox="0 0 8 12"><path d="M2 1l4 5-4 5" fill="none" stroke="#fff" stroke-width="2.2"/></svg></span></div>
  <div class="skin-photo" role="img" aria-label="Woman resting her chin on her hand beside aloe vera leaves"></div>
  <p class="skin-text">It is a long established fact that a reader will be distracted by the readable content of a page when looking at its layout.<br>It is a long established fact that a reader will be distracted by the readable content</p>
  <span class="btn-more">READ MORE</span>
</div>

<div class="abs panel" style="left:619px;width:465px">
  <h3 class="script">Client Testimonial</h3>
  <div class="arrows" style="right:20px"><span class="arrow-dot"><svg width="8" height="12" viewBox="0 0 8 12"><path d="M6 1L2 6l4 5" fill="none" stroke="#fff" stroke-width="2.2"/></svg></span><span class="arrow-dot"><svg width="8" height="12" viewBox="0 0 8 12"><path d="M2 1l4 5-4 5" fill="none" stroke="#fff" stroke-width="2.2"/></svg></span></div>
  <div class="quote">It is a long established fact that a reader will be distracted by the readable content of a page when looking at its layout. It is a long established fact that a reader will be distracted by the readable content of a page</div>
  <div class="who">LOREN IPSUM<span>Dolar Sit</span></div>
  <div class="avatar" role="img" aria-label="Client portrait"></div>
</div>

<div class="abs brands">
  <svg class="abs" style="left:0;top:20px" width="14" height="22" viewBox="0 0 14 22"><path d="M11 2L3 11l8 9" fill="none" stroke="#111" stroke-width="3"/></svg>
  <div class="abs brand-name" style="left:50px">Lumera</div>
  <div class="abs brand-name" style="left:280px">Dermavia</div>
  <div class="abs brand-name" style="left:500px">Velastine</div>
  <div class="abs brand-name" style="left:720px">Clarelle</div>
  <svg class="abs" style="left:948px;top:20px" width="14" height="22" viewBox="0 0 14 22"><path d="M3 2l8 9-8 9" fill="none" stroke="#111" stroke-width="3"/></svg>
</div>

<footer class="abs footer">
  <div class="abs fcol" style="left:118px"><h5>INFORMATION</h5><ul><li>Home</li><li>About Us</li><li>Products</li><li>Serivies</li><li>Blog</li><li>Contact Us</li></ul></div>
  <div class="abs fcol" style="left:308px"><h5>MY ACCOUNT</h5><ul><li>Create Your Account</li><li>Log In</li><li>Sign In</li><li>Terms &amp; Conditions</li><li>Privacy Policy</li></ul></div>
  <div class="abs fcol" style="left:496px"><h5>SUBSCRIE OUR NEWSLETTER</h5></div>
  <div class="abs fcol" style="left:882px"><h5>FOLLOW US</h5></div>
</footer>
<div class="abs news">enter your e-mail address
  <span class="send"><svg style="margin:10px 0 0 18px" width="22" height="20" viewBox="0 0 22 20"><path d="M1 9L21 1l-6 18-4-7z" fill="#222"/></svg></span>
</div>
<div class="abs social" aria-label="Social media links"><span></span><span></span><span></span><span></span></div>

<div class="abs bottombar">
  <div class="abs copy">Copyright2017.All Right Reserved</div>
  <div class="abs pay" aria-label="Accepted payment methods"><span></span><span></span><span></span><span></span><span></span></div>
</div>

</body>
</html>
```